Business card for Luxury Portable Restroom Trailer company

We are a Luxury Portable Restroom Trailer Company Called PELIKAR HIRES. Based in Orange County California. We provide portable restroom trailers for events, such as, Weddings, Concerts, Charity events, Sporting events, Tournaments, Corporate events, ect. We rent and Sell the Luxury restrooms. Our colors are white, grey, and Orange. As you will see in the logo we uploaded.
There are 2 people in the company so the names and titles will change for the 3 people but card will remain the same. Here is the information for each Person: Dennis Moyle CFO 555 018-3647
next Person: Wesley Tanford VP 555 018-3647
Next Person: Miles Tanford CEO 555 018-3647
Information to include on the card: Luxury Restroom Trailers Rental and Sales. Weddings, Concerts, Charity, Sporting and Corp. Events.

```html
<!DOCTYPE html>
<html lang="en">
<head>
<meta charset="utf-8">
<title>Pelikar Hires – Business Card</title>
<link rel="stylesheet" href="https://fonts.googleapis.com/css2?family=Lato:wght@400;700;900&family=Montserrat:wght@500;700&display=swap">
<style>
  :root{
    --bg:#2c2d30;
    --card-white:#ffffff;
    --card-grey:#5a5a5c;
    --band-grey:#6b6b6e;
    --ink:#2b2b2b;
    --orange:#f26522;
    --faint:#ededee;
    --light-text:#f4f4f4;
    --soft-text:#d9d9db;
  }
  *{margin:0;padding:0;box-sizing:border-box}
  html,body{width:1200px;height:952px;overflow:hidden;background:var(--bg)}
  .canvas{position:relative;width:1200px;height:952px;font-family:"Lato",sans-serif}

  .card{position:absolute;top:327px;width:520px;height:297px;border-radius:18px;overflow:hidden;
        box-shadow:0 14px 30px rgba(0,0,0,.45)}
  .card--front{left:50px;background:var(--card-white)}
  .card--back{left:630px;background:var(--card-grey);display:flex;flex-direction:column;
              align-items:center;justify-content:center;gap:18px}

  /* front */
  .watermark{position:absolute;left:0;top:88px;width:230px;height:209px;
             background:linear-gradient(160deg,#f3f3f4,var(--faint));border-top-right-radius:60px}
  .brand{position:absolute;left:28px;top:26px;display:flex;align-items:center;gap:10px;
         border:3px solid var(--ink);padding:7px 14px 7px 10px;background:var(--card-white)}
  .brand__dot{width:14px;height:14px;background:var(--orange)}
  .brand__name{font-weight:900;font-size:24px;letter-spacing:1px;color:var(--ink)}

  .person{position:absolute;right:34px;top:98px;text-align:right}
  .person__name{font-family:"Montserrat",sans-serif;font-weight:500;font-size:19px;letter-spacing:1.5px;color:var(--ink)}
  .person__name strong{font-weight:700;color:var(--orange)}
  .person__title{font-size:14px;color:var(--ink);margin-top:4px}
  .person__rule{width:52px;height:1.5px;background:var(--ink);margin:8px 0 0 auto}

  .address{position:absolute;right:34px;top:176px;display:flex;align-items:center;gap:8px;
           font-size:11.5px;line-height:1.35;color:var(--ink);text-align:right}

  .contact-band{position:absolute;left:235px;right:0;top:222px;bottom:0;background:var(--band-grey);
                border-top-left-radius:26px;padding:10px 34px 0 0}
  .contact{list-style:none}
  .contact li{display:flex;justify-content:flex-end;align-items:center;gap:8px;
              font-size:11.5px;color:var(--light-text);height:20px}

  .icon{width:17px;height:17px;flex:none;background:var(--orange);border-radius:3px;
        display:flex;align-items:center;justify-content:center}
  .icon svg{width:11px;height:11px}

  /* back */
  .back__brand{display:flex;align-items:center;gap:16px}
  .back__ring{width:34px;height:34px;border:4px solid var(--orange);border-radius:50%}
  .back__name{font-weight:900;font-size:26px;letter-spacing:1.5px;color:var(--orange)}
  .back__services{text-align:center;line-height:1.5}
  .back__tagline{font-weight:700;font-size:14px;letter-spacing:.5px;color:var(--light-text)}
  .back__events{font-size:12px;color:var(--soft-text)}
</style>
</head>
<body>
<main class="canvas">

  <section class="card card--front" aria-label="Card front">
    <div class="watermark" role="img" aria-label="Faint large brand emblem watermark"></div>

    <div class="brand">
      <span class="brand__dot"></span>
      <span class="brand__name">PELIKAR HIRES</span>
    </div>

    <div class="person">
      <p class="person__name">DENNIS <strong>MOYLE</strong></p>
      <p class="person__title">CFO</p>
      <div class="person__rule"></div>
    </div>

    <div class="address">
      <p>2170 Harbor Crest Avenue<br>Irvine, CA 92614</p>
      <span class="icon"><svg viewBox="0 0 12 12"><path d="M6 1a3.5 3.5 0 0 0-3.5 3.5C2.5 7 6 11 6 11s3.5-4 3.5-6.5A3.5 3.5 0 0 0 6 1zm0 4.8a1.3 1.3 0 1 1 0-2.6 1.3 1.3 0 0 1 0 2.6z" fill="#fff"/></svg></span>
    </div>

    <div class="contact-band">
      <ul class="contact">
        <li>555 018-3647
          <span class="icon"><svg viewBox="0 0 12 12"><path d="M3 1.5l1.6 2.2-.9 1.1a6 6 0 0 0 3.5 3.5l1.1-.9 2.2 1.6-.8 1.6C6 10.4 1.6 6 1.4 2.3z" fill="#fff"/></svg></span></li>
        <li>hello@pelikarhires.com
          <span class="icon"><svg viewBox="0 0 12 12"><rect x="1.5" y="3" width="9" height="6" fill="none" stroke="#fff" stroke-width="1.2"/><path d="M1.5 3L6 6.5 10.5 3" fill="none" stroke="#fff" stroke-width="1.2"/></svg></span></li>
        <li>www.pelikarhires.com
          <span class="icon"><svg viewBox="0 0 12 12"><path d="M3 1.5l6 5-2.6.3 1.5 3-1.2.6-1.5-3-2 1.7z" fill="#fff"/></svg></span></li>
      </ul>
    </div>
  </section>

  <section class="card card--back" aria-label="Card back">
    <div class="back__brand">
      <span class="back__ring"></span>
      <span class="back__name">PELIKAR HIRES</span>
    </div>
    <div class="back__services">
      <p class="back__tagline">Luxury Restroom Trailers Rental and Sales</p>
      <p class="back__events">Weddings, Concerts, Charity, Sporting and Corp. Events</p>
    </div>
  </section>

</main>
</body>
</html>
```